Capital Management company needs a web design

We have a domain name and logo but need hosting and design. Please look at the Must-Haves section.

Target Market(s)

banking industry and investors

Industry/Entity Type

Investment

Coding

Coded - Design and coding required

Number of Pages Required

1 page

Font styles to use
Sans Serif

Requirements
Must have
• Picture(s) of skyscraper skyline (can be of Manhattan, Chicago, or any other major city in the USA).
• Please use the three colors of the logo as a backdrop to part of the webpage(s)
Should not have
• No "what our clients say" section
• No pictures of people

```html
<!DOCTYPE html>
<html lang="en">
<head>
<meta charset="utf-8">
<title>Harbor Crest Capital – Contact</title>
<link href="https://fonts.googleapis.com/css2?family=Mulish:wght@400;600;700&display=swap" rel="stylesheet">
<style>
  :root {
    --brand-blue: #1f7fc4;
    --link-blue: #2379c0;
    --ink: #111111;
    --ink-soft: #333333;
    --white: #ffffff;
    --header-bg: rgba(52, 62, 72, 0.9);
    --tab-bg: rgba(10, 10, 10, 0.82);
    --tab-border: rgba(255, 255, 255, 0.55);
  }
  * { margin: 0; padding: 0; box-sizing: border-box; }
  html, body { width: 1200px; height: 621px; overflow: hidden; }
  body { font-family: "Mulish", sans-serif; position: relative; background: #2c2f36; }

  .skyline {
    position: absolute; inset: 0;
    background:
      radial-gradient(ellipse 220px 120px at 965px 108px, rgba(255, 210, 120, 0.85), rgba(255, 170, 80, 0) 70%),
      linear-gradient(180deg, #b77a4a 0%, #d69a5c 14%, #8a7a72 26%, #5d5a5e 45%, #4a3f3d 70%, #3a302e 100%);
  }

  .site-header {
    position: absolute; left: 0; top: 0; width: 1200px; height: 71px;
    background: var(--header-bg);
  }
  .brand {
    position: absolute; left: 141px; top: 22px;
    color: var(--white); font-weight: 700; font-size: 20px; letter-spacing: 0.5px;
    display: flex; align-items: center; gap: 8px;
  }
  .brand-mark { width: 10px; height: 10px; background: var(--white); }
  .main-nav {
    position: absolute; top: 30px; left: 685px;
    display: flex; gap: 29px; list-style: none;
  }
  .main-nav li {
    color: var(--white); font-size: 10.5px; font-weight: 600; letter-spacing: 0.2px;
  }

  .contact-card {
    position: absolute; left: 141px; top: 112px; width: 318px; height: 396px;
    background: var(--white);
  }
  .contact-title {
    position: absolute; left: 15px; top: 22px;
    color: var(--brand-blue); font-size: 14px; font-weight: 700; letter-spacing: 0.3px;
  }
  .office-map {
    position: absolute; left: 14px; top: 55px; width: 290px; height: 81px;
    background: linear-gradient(90deg, #e9e6df 0%, #ecebe6 60%, #a9d3f0 78%, #9fcdee 100%);
  }
  .contact-group { position: absolute; left: 14px; font-size: 11px; line-height: 15px; }
  .contact-group dt { color: var(--ink); font-weight: 600; }
  .contact-group dd { color: var(--link-blue); }
  .contact-group dd.address { color: var(--ink-soft); line-height: 14px; }

  .section-tabs { position: absolute; top: 515px; left: 141px; }
  .tab {
    position: absolute; top: 0; width: 127px; height: 71px;
    background: var(--tab-bg); border: 1px solid var(--tab-border);
    color: var(--white); font-size: 10.5px; font-weight: 600; letter-spacing: 0.2px;
    display: flex; flex-direction: column; align-items: center; justify-content: center;
  }
  .tab.is-active { background: var(--brand-blue); border-color: var(--brand-blue); padding-top: 4px; }
  .tab-icon { margin-bottom: 6px; }
</style>
</head>
<body>
  <div class="skyline" role="img" aria-label="Aerial photograph of a city skyline of skyscrapers at sunset"></div>

  <header class="site-header">
    <div class="brand"><span class="brand-mark"></span>Harbor Crest Capital</div>
    <ul class="main-nav">
      <li>PAY PROPERTY TAXES</li>
      <li>TAX LIEN ASSIGNMENTS</li>
      <li>REO</li>
      <li>LOGIN</li>
    </ul>
  </header>

  <section class="contact-card">
    <h2 class="contact-title">CONTACT</h2>
    <div class="office-map" role="img" aria-label="Street map showing the office location"></div>

    <dl class="contact-group" style="top:155px">
      <dt>Prospective Investors</dt>
      <dd>info@harborcrestcapital.com</dd>
    </dl>
    <dl class="contact-group" style="top:196px">
      <dt>Municipalities</dt>
      <dd>servicing@harborcrestcapital.com</dd>
    </dl>
    <dl class="contact-group" style="top:236px">
      <dt>Propery Owners/Taxpayers</dt>
      <dd>Click Here</dd>
    </dl>
    <dl class="contact-group" style="top:276px">
      <dt>Mortgage Compaies/Attorneys(Lender)</dt>
      <dd>legal@harborcrestcapital.com</dd>
    </dl>
    <dl class="contact-group" style="top:331px">
      <dt>Corporate Office:</dt>
      <dd class="address">123, lorem Ipsume dollor site 2215<br>lorem ipsume, usa 300008</dd>
    </dl>
  </section>

  <nav class="section-tabs">
    <div class="tab" style="left:0">ABOUT US</div>
    <div class="tab" style="left:141px">SERVICES</div>
    <div class="tab" style="left:283px">INVESTMENT</div>
    <div class="tab is-active" style="left:424px">
      <svg class="tab-icon" width="12" height="11" viewBox="0 0 12 11" aria-hidden="true">
        <path d="M1 5 L6 1 L11 5 M1 10 L6 6 L11 10" fill="none" stroke="#fff" stroke-width="1.6"/>
      </svg>
      CONTACT
    </div>
  </nav>
</body>
</html>
```